Redesign of Plastic Surgeon Website to fully responsive / modern feel

Hi

Our current website is out of date www.harbourlinecosmetic.org

We want a fresh / modern looking design
Needs to be fully responsive design that works extremely well on ipad and mobile device

Would like design for both full screen website and mobile

Have listed a few websites of other plastic surgeons we like
http://www.reformclinicdaily.com/
http://www.peterholtbymd.com/
http://www.corvanbeauty.com/
http://www.tidewellcontouring.com/

Menu needs to include
1. About Us
2. Procedures (see current website for example)
3. News
4. Patient Resources
5. Contact Us

We are flexible with colours / images / layout

I have uploaded a document that has some content - the face pages content is completed only

some of the procedures can have content upwards of 4000 words - total website can be large with over 40,000 words
Updates

Target Market(s)

Mainly women 20-60 85% of practice
Some men 15%

Industry/Entity Type

Plastic Surgery

Number of Pages Required

5+ page

Requirements
Must have
• We need designs for
• Homepage
• Internal pages
• 1. Landing pages for breast / body / face / non surgical main pages
• 2. Procedure pages for individual pages under each section - eg breast augmentation
• 3. About us pages - like meet the doctor, our staff, clinics
• 4. Contact page
• 5. Blog / News page
Nice to have
• See our list of websites for examples of designs we like
• Like full screen design with nice hero image
• Needs to have good to call to action messages on home page like
• Specials, procedure of the month, etc

```html
<!DOCTYPE html>
<html lang="en">
<head>
<meta charset="utf-8">
<title>Harbourline Institute of Cosmetic Surgery</title>
<link rel="stylesheet" href="https://fonts.googleapis.com/css2?family=Cinzel:wght@400;700&family=Lato:wght@400;700&display=swap">
<style>
:root{
  --ink:#231f1c;
  --ink-soft:#3b3733;
  --gold:#7b6b48;
  --gold-light:#9c875a;
  --gold-line:#a8946a;
  --paper:#ffffff;
  --mist:#f1f1f1;
  --sand:#f3efe6;
  --text:#3a3a3a;
  --muted:#8a8a8a;
  --rule:#d8d8d8;
}
*{box-sizing:border-box;margin:0;padding:0}
html,body{width:721px;height:1200px;overflow:hidden;background:var(--paper)}
body{font-family:"Lato",sans-serif;color:var(--text);position:relative}
.abs{position:absolute}
.caps{font-family:"Cinzel",serif}

/* header */
.site-header{left:0;top:0;width:721px;height:70px;background:var(--ink);border-bottom:2px solid var(--gold-line)}
.brand{left:79px;top:0;width:78px;height:114px;background:var(--ink);z-index:3;padding:6px 4px 0;text-align:center;clip-path:polygon(0 0,100% 0,100% 92%,50% 100%,0 92%)}
.brand span{display:block;font-family:"Cinzel",serif;font-size:10.5px;line-height:15px;color:#e9e2d2;letter-spacing:.3px}
.contact-top{right:79px;top:5px;text-align:right;color:#f2efe8;font-size:11px;line-height:20px}
.contact-top .phone{font-size:12px}
.contact-top svg{vertical-align:-2px;margin-right:5px}
.main-nav{right:79px;top:46px;display:flex;align-items:center;font-family:"Cinzel",serif;font-size:10px;color:#e9e2d2}
.main-nav a{color:inherit;text-decoration:none;padding:0 6px}
.main-nav a.active{background:var(--gold);padding:3px 6px;margin-right:10px}
.main-nav i{color:#777;font-style:normal}

/* hero */
.hero{left:0;top:72px;width:721px;height:313px;background:linear-gradient(90deg,#8e8e8e 0%,#c9c9c9 25%,#f4f2f0 55%,#fbf9f7 100%)}
.hero-photo{left:300px;top:72px;width:421px;height:313px;background:radial-gradient(ellipse at 55% 40%,#e9c9b4 0%,#d5a98c 18%,#f3ece6 46%,rgba(255,255,255,0) 70%)}
.slide-tag{left:79px;width:209px;height:33px;background:#0e0d0c;color:#f5f1ea;font-family:"Cinzel",serif;font-size:19px;letter-spacing:1px;line-height:33px;padding-left:8px}
.slide-arrow{width:24px;height:24px;border-radius:50%;background:#2f2d2b;display:flex;align-items:center;justify-content:center}

/* procedure cards */
.card{top:404px;width:180px;height:107px;border:1px solid #cfcfcf;box-shadow:0 4px 6px rgba(0,0,0,.12)}
.card .ph{height:88px}
.card .label{height:19px;background:var(--ink);color:#f1ece2;text-align:center;font-family:"Cinzel",serif;font-size:13px;line-height:19px;letter-spacing:.5px}

/* welcome */
.welcome{left:0;top:540px;width:721px;height:165px;background:linear-gradient(#ececec,#fafafa 60%,#fff)}
.welcome h1{position:absolute;left:0;top:20px;width:721px;text-align:center;font-family:"Cinzel",serif;font-weight:400;font-size:15px;color:var(--ink)}
.welcome h1 em{font-style:normal;color:var(--gold-light)}
.welcome .line{position:absolute;left:260px;top:44px;width:200px;height:1px;background:linear-gradient(90deg,transparent,#bbb,transparent)}
.welcome p{position:absolute;left:82px;top:56px;width:558px;font-size:8.3px;line-height:13.5px;text-align:center;color:#444}
.btn{background:var(--gold);color:#fff;font-size:8.5px;font-weight:700;text-align:center;border-radius:2px;line-height:16px;height:16px}

/* columns */
.col-title{top:722px;font-family:"Cinzel",serif;font-size:12.5px;color:var(--ink)}
.col-title em{font-style:normal;color:var(--gold-light)}
.col-rule{top:720px;width:1px;height:165px;background:#e3e3e3}
.frame{border:1px solid #d0d0d0;padding:2px;background:#fff}
.small{font-size:7.6px;line-height:10.5px;color:var(--muted)}
.field{left:469px;width:173px;height:24px;border:1px solid #ddd;border-top:none;display:flex;align-items:center;font-size:7.4px;color:#aaa}
.field .ico{width:24px;height:24px;background:#6b5d41;display:flex;align-items:center;justify-content:center;margin-right:8px;margin-left:-1px}

/* testimonials */
.testi{left:79px;top:913px;width:563px;height:31px;border:1px solid #cfcfcf;background:linear-gradient(#fafafa,#ececec)}
.testi-tab{left:79px;top:913px;width:121px;height:31px;background:var(--gold);color:#fff;font-family:"Cinzel",serif;font-size:12px;line-height:31px;padding-left:11px;clip-path:polygon(0 0,88% 0,100% 50%,88% 100%,0 100%)}
.testi p{position:absolute;left:126px;top:5px;width:360px;font-size:7.3px;line-height:10.5px;font-style:italic;color:#555}
.mini{width:11px;height:11px;border:1px solid #ccc;background:#fff;font-size:7px;line-height:9px;text-align:center;color:#888}

/* partners */
.partners{left:0;top:974px;width:721px;height:101px;background:var(--sand)}
.partners-tab{left:309px;top:968px;width:131px;height:24px;background:var(--gold);color:#fff;font-family:"Cinzel",serif;font-size:14px;text-align:center;line-height:24px;border-radius:0 0 4px 4px;box-shadow:0 0 0 2px #fff}
.badge{top:1005px;background:#d9d4c8;opacity:.8}

/* footer */
.site-footer{left:0;top:1075px;width:721px;height:125px;background:var(--ink-soft);border-bottom:3px solid #6d6355;color:#eee}
.f-title{top:16px;font-family:"Cinzel",serif;font-size:10px;letter-spacing:.5px;padding-bottom:6px;border-bottom:1px dashed #777}
.f-list{top:42px;font-size:7.8px;line-height:12px;list-style:none}
.f-list li::before{content:"› ";color:#bbb}
.social{font-size:8px;font-weight:700;display:flex;align-items:center}
.social b{width:11px;height:11px;background:#eee;border-radius:2px;margin-right:7px;display:inline-block}
</style>
</head>
<body>

<header class="site-header abs"></header>
<div class="brand abs"><span>Harbourline</span><span>Institute</span><span>of</span><span>Cosmetic</span><span>Surgery</span></div>
<div class="contact-top abs">
  <div class="phone"><svg width="11" height="11" viewBox="0 0 24 24"><path fill="#a8946a" d="M6.6 10.8a15 15 0 0 0 6.6 6.6l2.2-2.2a1 1 0 0 1 1-.25 11.4 11.4 0 0 0 3.6.57 1 1 0 0 1 1 1V20a1 1 0 0 1-1 1A17 17 0 0 1 3 4a1 1 0 0 1 1-1h3.5a1 1 0 0 1 1 1c0 1.25.2 2.45.57 3.6a1 1 0 0 1-.25 1z"/></svg>+61 (02) 9000 4821</div>
  <div><svg width="13" height="9" viewBox="0 0 13 9"><rect width="13" height="9" fill="#a8946a"/><path d="M0 0l6.5 5L13 0" stroke="#231f1c" fill="none"/></svg>info@harbourlinecosmetic.org</div>
</div>
<nav class="main-nav abs">
  <a class="active">Home</a><a>About Us</a><i>|</i><a>Procedures</a><i>|</i><a>News</a><i>|</i><a>Patient Resources</a><i>|</i><a>Contact Us</a>
</nav>

<section class="hero abs"></section>
<div class="hero-photo abs" role="img" aria-label="Hero photograph: woman with long auburn hair resting on white bedding"></div>
<div class="slide-tag abs" style="top:168px">Face Treatment</div>
<div class="slide-tag abs" style="top:207px">Body Treatment</div>
<div class="slide-tag abs" style="top:247px">Breast Surgery</div>
<div class="slide-arrow abs" style="left:36px;top:211px"><svg width="8" height="10"><path d="M6 1L2 5l4 4" stroke="#fff" stroke-width="1.6" fill="none"/></svg></div>
<div class="slide-arrow abs" style="left:660px;top:217px"><svg width="8" height="10"><path d="M2 1l4 4-4 4" stroke="#fff" stroke-width="1.6" fill="none"/></svg></div>

<div class="card abs" style="left:79px"><div class="ph" role="img" aria-label="Close-up photo of a woman's eye for face treatment" style="background:linear-gradient(135deg,#e8cdb6,#c99f83 60%,#8fb3cf)"></div><div class="label">Face Treatment</div></div>
<div class="card abs" style="left:271px"><div class="ph" role="img" aria-label="Photo of a torso marked for body contouring" style="background:linear-gradient(#d4a88a,#e8c4a8 50%,#c98f73)"></div><div class="label">Body Treatment</div></div>
<div class="card abs" style="left:462px"><div class="ph" role="img" aria-label="Photo illustrating breast surgery" style="background:linear-gradient(135deg,#f6eee8,#e6c2aa 55%,#d8a88c)"></div><div class="label">Breast Surgery</div></div>

<section class="welcome abs">
  <h1>Welcome To <em>Harbourline Institute Of Cosmetic Surgery</em></h1>
  <div class="line"></div>
  <p>You can expect beautiful results at the Harbourline Institute of Cosmetic Surgery. With expertise in facelifts, breast augmentation or breast reduction and liposuction body contouring, we offer total care at every step of your transformative journey. Dr Ashcroft is one of Australia's most eminent specialists in plastic surgery, reconstructive and aesthetic surgery, and is supported by our highly qualified, professional team. As the premier plastic surgery clinic in Sydney, we use only the most revolutionary techniques to minimise scarring, we help you look better, feel better and enjoy a beautiful new you.</p>
  <div class="btn abs" style="left:337px;top:126px;width:68px">READ MORE</div>
</section>
<div class="abs" style="left:79px;top:702px;width:563px;height:1px;background:#e6e6e6"></div>

<div class="col-title abs" style="left:79px">Our <em>Specialist</em></div>
<div class="col-rule abs" style="left:261px"></div>
<div class="frame abs" style="left:79px;top:746px;width:174px;height:70px"><div role="img" aria-label="Photo of the specialist standing on a rocky seashore" style="width:100%;height:100%;background:linear-gradient(#d9dde2,#9aa3ab 55%,#4a4640)"></div></div>
<div class="abs" style="left:80px;top:821px;font-size:10.5px;font-weight:700;color:#222">Dr. Graham Ashcroft</div>
<div class="small abs" style="left:80px;top:837px;width:170px">Lorem ipsum dolor sit amet, consectetur adipisi cing elit,sed do eiusmod tempor incididunt utst lab ore et dolo...</div>
<div class="btn abs" style="left:203px;top:869px;width:50px">Read More</div>

<div class="col-title abs" style="left:274px">View <em>Video</em></div>
<div class="col-rule abs" style="left:456px"></div>
<div class="frame abs" style="left:273px;top:746px;width:175px;height:102px">
  <div role="img" aria-label="Video still of lips receiving a filler injection" style="width:100%;height:82px;background:linear-gradient(90deg,#e7c3b1,#f2e4dc 55%,#e2cde0)"></div>
  <div style="height:15px;background:#111;display:flex;align-items:center;color:#fff;font-size:6.5px;padding:0 5px;gap:6px">
    <svg width="7" height="8"><path d="M0 0l7 4-7 4z" fill="#fff"/></svg><span>04:59</span><span style="flex:1;height:4px;background:#444;border-radius:2px"></span><span>10:35</span>
  </div>
</div>
<div class="abs" style="left:345px;top:777px;width:28px;height:28px;border-radius:50%;background:#fff;display:flex;align-items:center;justify-content:center"><svg width="9" height="11"><path d="M0 0l9 5.5L0 11z" fill="#111"/></svg></div>
<div class="small abs" style="left:274px;top:853px">Lorem ipsum dolor sit amet, consectetur</div>
<div class="btn abs" style="left:397px;top:869px;width:50px">View All</div>

<div class="col-title abs" style="left:469px">Make <em>An Appointment</em></div>
<div class="abs" style="left:469px;top:746px;width:173px;height:1px;background:#ddd"></div>
<div class="field abs" style="top:746px"><span class="ico"><svg width="10" height="10"><circle cx="5" cy="3" r="2.5" fill="#fff"/><path d="M0 10a5 4 0 0 1 10 0z" fill="#fff"/></svg></span>Full Name</div>
<div class="field abs" style="top:770px"><span class="ico"><svg width="11" height="8"><rect x=".5" y=".5" width="10" height="7" fill="none" stroke="#fff"/><path d="M.5.5l5 4 5-4" stroke="#fff" fill="none"/></svg></span>Email Address</div>
<div class="field abs" style="top:794px"><span class="ico"><svg width="10" height="10"><rect x=".5" y="1.5" width="9" height="8" fill="none" stroke="#fff"/><path d="M.5 3.5h9M3 0v3M7 0v3" stroke="#fff"/></svg></span>Appointment Date</div>
<div class="field abs" style="top:818px;height:52px;align-items:flex-start"><span class="ico" style="height:24px"><svg width="10" height="8"><path d="M0 1h10M0 4h10M0 7h7" stroke="#fff" stroke-width="1.4"/></svg></span><span style="margin-top:8px">Message</span></div>
<div class="btn abs" style="left:569px;top:869px;width:73px;height:18px;line-height:18px">SEND MESSAGE</div>

<div class="testi abs"><p>" Lorem ipsum dolor sit amet, consectetuer adipiscing elit, sed diam nonummy nibh euismod tincidunt ut laoreet dolore magna aliquam erat volutpat. Ut wisi enim ad minim veniam, "</p>
  <div class="mini abs" style="left:528px;top:10px">‹</div><div class="mini abs" style="left:543px;top:10px">›</div>
</div>
<div class="testi-tab abs">Testimonials</div>

<section class="partners abs"></section>
<div class="partners-tab abs">Our Partners</div>
<div class="abs" style="left:55px;top:1026px;color:#aaa;font-size:12px">‹</div>
<div class="abs" style="left:657px;top:1026px;color:#aaa;font-size:12px">›</div>
<div class="badge abs" style="left:82px;width:76px;height:56px;border-radius:28px"></div>
<div class="badge abs" style="left:189px;width:62px;height:62px;border-radius:50%"></div>
<div class="badge abs" style="left:286px;width:118px;height:46px;top:1013px"></div>
<div class="badge abs" style="left:435px;width:62px;height:50px;border-radius:50%;opacity:.5"></div>
<div class="badge abs" style="left:530px;width:112px;height:52px"></div>

<footer class="site-footer abs">
  <div class="f-title abs" style="left:82px;width:78px">Quick Links</div>
  <ul class="f-list abs" style="left:80px"><li>Home</li><li>About Us</li><li>Procedures</li><li>News</li><li>Patient Resources</li><li>Contact Us</li></ul>

  <div class="f-title abs" style="left:199px;width:123px">Contact Details</div>
  <div class="abs" style="left:199px;top:42px;font-size:7.8px;line-height:11px">
    <div style="display:flex;gap:8px"><svg width="8" height="10"><path d="M4 0a4 4 0 0 1 4 4c0 3-4 6-4 6S0 7 0 4a4 4 0 0 1 4-4z" fill="#ddd"/><circle cx="4" cy="4" r="1.5" fill="#3b3733"/></svg><span>Wexley Clinic Suite 310<br>14 Ferry Lane<br>Kirribilli 2061</span></div>
    <div style="display:flex;gap:8px;margin-top:3px"><svg width="8" height="9" viewBox="0 0 24 24"><path fill="#ddd" d="M6.6 10.8a15 15 0 0 0 6.6 6.6l2.2-2.2a1 1 0 0 1 1-.25 11.4 11.4 0 0 0 3.6.57 1 1 0 0 1 1 1V20a1 1 0 0 1-1 1A17 17 0 0 1 3 4a1 1 0 0 1 1-1h3.5a1 1 0 0 1 1 1c0 1.25.2 2.45.57 3.6a1 1 0 0 1-.25 1z"/></svg><span>+61 (02) 9000 4821</span></div>
    <div style="display:flex;gap:8px;margin-top:2px"><svg width="10" height="7"><rect width="10" height="7" fill="#ddd"/><path d="M0 0l5 4 5-4" stroke="#3b3733" fill="none"/></svg><span>info@harbourlinecosmetic.org</span></div>
  </div>

  <div class="f-title abs" style="left:366px;width:88px">Follow Us</div>
  <div class="social abs" style="left:366px;top:42px"><b></b>Circlefeed</div>
  <div class="social abs" style="left:366px;top:64px"><b></b>Chirpline</div>
  <div class="social abs" style="left:366px;top:85px"><b></b>Linkwork</div>

  <div class="f-title abs" style="left:494px;width:126px">Newsletter Sign Up</div>
  <div class="abs" style="left:493px;top:40px;width:109px;height:15px;background:#fff;border-radius:2px;color:#555;font-size:7.5px;font-style:italic;line-height:15px;padding-left:4px">Email Address</div>
  <div class="btn abs" style="left:493px;top:62px;width:50px;height:14px;line-height:14px">Subscribe</div>
  <div class="abs" style="left:478px;top:89px;width:166px;text-align:center;font-size:7.6px;line-height:11.5px">Copyright © 2016 Harbourline Institute of Cosmetic Surgery. All Rights Reserved.</div>
</footer>

</body>
</html>
```